Australian Consultant Pharmacist Business Needs A3 Flyer for Medical Centre

Our business has just secured a deal in a medical centre to offer our consulting services. We have installed our software on the doctors computers and would like to have an A3 flyer to put on their walls to remind them about our services and explain very briefly how to use our simple software.

We would like the flyer to be vibrant and very simple whilst conveying our message of improving patient health outcomes and illustrating how to use our software and service.

We provide Home Medicine Reviews (HMR) for General Practitioners (GP) at medical centres.

There are 3 pathways for a GP to use our service, all resulting in the same outcome.

The outcome is the Dr sends us a referral for a HMR for their patient. In turn they receive a report back after we have performed the HMR.

Pathways
1.
-GP Opens Patient File in medical prescribing software
-If patient is eligible for a HMR, an alert will pop up in bottom right hand corner (approx 30 seconds)
- Click Send Referral
- New page opens, select reason for referral ie. several medicines
- Press Send - referral is sent electronically to Pharmacist

2.
No alert pops up but GP still wants to refer.
Right click Chime Notify program - Chime Notify program is identified by the bell shape icon in the bottom right side of the desktop tray next to the time.
Click refer current patient - this will refer the patient currently open on the GP prescribing software

3. GP would like to send HMR Referal via Fax.
Fax number 03 7192 3048

I have attached some examples of how the software and service works, including screen shots and some power points. I would like to use these as ideas for our A3 Flyer.

Good Luck!

Target Market(s)

Doctors

Industry/Entity Type

Health Service

Colors
f37122
0455a3
3176b5
33a6d7
f68d4c

Requirements
Must have
• Our company name - Brightwell Care HMR
• Our email brightwellcarehmr@fernmail.example
• our fax number
• the 3 ways to use our service and how
• prefer images and short keyword descriptions
• convey idea of improving patient health
• ensure our service comes accross as simple and effecient
Nice to have
• images, vibrant,
Should not have
• lengthy descriptions

```html
<!DOCTYPE html>
<html lang="en">
<head>
<meta charset="utf-8">
<title>Brightwell Care HMR – Flyer</title>
<link rel="stylesheet" href="https://fonts.googleapis.com/css2?family=Lato:ital,wght@0,400;0,700;0,900;1,700;1,900&family=Roboto+Condensed:wght@400;700&display=swap">
<style>
:root{
  --orange:#f37122;
  --orange-soft:#f68d4c;
  --navy:#0455a3;
  --blue:#3176b5;
  --sky:#33a6d7;
  --sky-pale:#8fd2f0;
  --ink:#2b2b2b;
  --white:#ffffff;
  --pill:#1c1f24;
}
*{box-sizing:border-box;margin:0;padding:0}
html,body{width:902px;height:1200px;overflow:hidden;background:#e9edf1}
body{font-family:"Lato",sans-serif;color:var(--ink)}
.flyer{position:relative;width:902px;height:1200px;overflow:hidden;background:var(--white)}

/* header */
.masthead{position:absolute;left:0;top:0;width:902px;height:348px;
  background:linear-gradient(135deg,#0a63b8 0%,var(--navy) 45%,#1b7cd0 100%)}
.brand-line{position:absolute;left:30px;top:50px;font-weight:900;font-size:36px;letter-spacing:1px;color:var(--white)}
.brand-mark{position:absolute;left:26px;top:76px;font-weight:900;font-size:168px;line-height:1;letter-spacing:-2px;color:var(--white)}
.tagline{position:absolute;left:30px;top:262px;font-weight:700;font-size:38px;line-height:1.15;color:var(--orange)}
.hero-photo{position:absolute;left:424px;top:24px;width:520px;height:320px;border-radius:160px 0 0 160px;
  border:8px solid var(--orange);border-right:none;
  background:linear-gradient(120deg,#d9d2c4 0%,#c9b9a2 35%,#e8e6e2 60%,#9fb3c8 100%)}
.header-rule{position:absolute;left:0;top:348px;width:902px;height:12px;background:var(--orange)}

/* left column */
.intro{position:absolute;left:28px;top:392px;font-size:21px;line-height:1.3}
.intro .lead{color:var(--navy)}
.pathways-band{position:absolute;left:0;top:452px;width:522px;height:82px;background:var(--sky);
  padding:14px 20px 0 28px;color:var(--white);font-style:italic;font-weight:700;font-size:19px;line-height:1.35}
.pathway-title{position:absolute;left:28px;display:flex;align-items:center;gap:8px;
  color:var(--orange);font-style:italic;font-weight:900;font-size:22px}
.pathway-num{width:36px;height:36px;border-radius:50%;background:var(--orange);color:var(--white);
  font-style:normal;font-size:26px;display:flex;align-items:center;justify-content:center}
.steps{position:absolute;left:28px;width:470px;list-style:none;font-size:14px;line-height:1.35}
.steps li{position:relative;padding-left:24px;margin-bottom:7px}
.steps li::before{content:"";position:absolute;left:2px;top:5px;width:9px;height:9px;border-radius:50%;background:var(--navy)}
.steps li.plain::before{display:none}
.fax-box{position:absolute;left:28px;top:1000px;width:494px;height:70px;background:var(--orange);color:var(--white);padding:8px 0 0 30px}
.fax-box .note{font-size:14px;position:relative;padding-left:0}
.fax-box .note::before{content:"";position:absolute;left:-22px;top:4px;width:9px;height:9px;border-radius:50%;background:var(--navy)}
.fax-box .fax{font-size:31px;line-height:1.2;margin-top:2px}

/* right column */
.guide{position:absolute;left:522px;top:360px;width:380px;height:720px;background:var(--sky)}
.guide-pill{position:absolute;left:602px;top:382px;width:300px;height:48px;border-radius:24px 0 0 24px;
  background:var(--pill);color:var(--white);font-family:"Roboto Condensed",sans-serif;font-size:25px;
  display:flex;align-items:center;padding-left:18px}
.step-panel{position:absolute;left:522px;width:380px;background:var(--sky-pale)}
.step-head{position:absolute;right:24px;display:flex;align-items:center;gap:10px;color:var(--white);
  font-style:italic;font-weight:900;font-size:19px}
.step-num{width:30px;height:24px;background:var(--navy);color:var(--white);font-style:normal;font-size:18px;
  display:flex;align-items:center;justify-content:center}
.screen{position:absolute;background:linear-gradient(180deg,#f4f7fa,#d7e2ec);border:2px solid #1b2430}
.callout{position:absolute;background:var(--orange);color:var(--white);font-size:11px;line-height:1.25;
  padding:4px 6px;text-align:center}
.tips{position:absolute;left:540px;top:818px;width:345px;list-style:none;text-align:right;
  font-style:italic;font-weight:700;font-size:12.5px;color:var(--ink);line-height:1.3}
.tips li{position:relative;padding-right:24px;margin-bottom:9px}
.tips li::after{content:"";position:absolute;right:2px;top:4px;width:8px;height:8px;border-radius:50%;background:var(--orange)}
.tray-steps{position:absolute;left:548px;top:1096px;display:grid;grid-template-columns:150px 150px;column-gap:6px;
  font-style:italic;font-weight:700;font-size:12.5px;color:var(--white);line-height:1.3}
.tray-steps b{color:var(--orange)}

/* footer */
.footer{position:absolute;left:0;top:1070px;width:902px;height:130px}
.email{position:absolute;left:30px;top:1140px;display:flex;align-items:baseline;gap:18px;font-style:italic}
.email .label{color:var(--orange);font-weight:900;font-size:28px}
.email .addr{color:var(--white);font-weight:700;font-size:22px}
</style>
</head>
<body>
<main class="flyer">

  <header class="masthead">
    <div class="brand-line">BRIGHTWELL CARE</div>
    <div class="brand-mark">HMR</div>
    <div class="tagline">Improving Patient<br>Outcomes</div>
    <div class="hero-photo" role="img" aria-label="Pharmacist in a white coat explaining a medicine bottle to an elderly couple in a pharmacy"></div>
  </header>
  <div class="header-rule"></div>

  <section class="guide" aria-label="How to use Chime Notify"></section>

  <svg class="footer" width="902" height="130" viewBox="0 0 902 130" aria-hidden="true">
    <path d="M0 18 C260 -4 620 -4 902 20 L902 130 L0 130 Z" fill="#0a63b8"/>
    <path d="M0 40 C300 20 620 22 902 44 L902 130 L0 130 Z" fill="#0455a3" opacity="0.55"/>
  </svg>

  <p class="intro"><span class="lead">We provide Home Medicine Reviews (HMR)</span><br>for General Practitioners (GP) at medical centres</p>

  <div class="pathways-band">There are 3 pathways for a GP to use our service,<br>all resulting in the same outcome</div>

  <h2 class="pathway-title" style="top:560px">Pathway <span class="pathway-num">1</span></h2>
  <ul class="steps" style="top:612px">
    <li>GP Opens Patient File in medical prescribing software</li>
    <li>If patient is eligible for a HMR, an alert will pop up in bottom right hand corner (approx 30 seconds)</li>
    <li>Click Send Referral</li>
    <li>New page opens, select reason for referral ie. several medicines</li>
    <li>Press Send - referral is sent electronically to Pharmacist</li>
  </ul>

  <h2 class="pathway-title" style="top:772px">Pathway <span class="pathway-num">2</span></h2>
  <ul class="steps" style="top:830px">
    <li>No alert pops up but GP still wants to refer.</li>
    <li>Right click Chime Notify program - Chime Notify program is identified by the bell shape icon in the bottom right side of the desktop tray next to the time.</li>
    <li class="plain">Click refer current patient - this will refer the patient currently open on the GP prescribing software</li>
  </ul>

  <h2 class="pathway-title" style="top:958px">Pathway <span class="pathway-num">3</span></h2>
  <div class="fax-box">
    <p class="note">GP would like to send HMR Referal via Fax</p>
    <p class="fax">Fax number 03 7192 3048</p>
  </div>

  <div class="guide-pill">How To Use Chime Notify</div>

  <div class="step-panel" style="top:444px;height:150px"></div>
  <div class="step-head" style="top:454px">Where is Chime Notify? <span class="step-num">1</span></div>
  <div class="screen" style="left:544px;top:492px;width:340px;height:62px" role="img" aria-label="Desktop taskbar showing the bell icon in the system tray"></div>
  <svg style="position:absolute;left:660px;top:478px" width="40" height="60" aria-hidden="true">
    <path d="M12 0 V28" stroke="#f37122" stroke-width="5"/><path d="M2 26 L12 44 L22 26 Z" fill="#f37122"/>
  </svg>

  <div class="step-panel" style="top:606px;height:210px"></div>
  <div class="step-head" style="top:616px">Chime Notify Pop Up <span class="step-num">2</span></div>
  <div class="screen" style="left:602px;top:650px;width:282px;height:112px" role="img" aria-label="Chime Notify alert pop-up window with Don't Refer, Send Referral and Disable Alerts buttons"></div>
  <div class="callout" style="left:548px;top:700px;width:90px">Don't refer – but alerts will still pop up for this patient</div>
  <div class="callout" style="left:646px;top:772px;width:110px">Opens the Send to Pharmacist Screen</div>
  <div class="callout" style="left:762px;top:772px;width:116px">Disable alerts for this patient for 12 months</div>

  <div class="step-head" style="top:830px;font-size:15px">Send Referral to Pharmacist <span class="step-num">3</span></div>
  <ul class="tips" style="top:866px">
    <li>This screen will appear after pressing send referral</li>
    <li>Once you press SEND, no further action is required</li>
    <li>You may choose to write a note in the patients file<br>that a HMR has been requested</li>
  </ul>
  <div class="screen" style="left:684px;top:968px;width:200px;height:100px" role="img" aria-label="Send to Pharmacist referral form with clinical need checkboxes and a Send button"></div>
  <div class="callout" style="left:588px;top:980px;width:66px;font-size:12px">Press Send</div>
  <div class="callout" style="left:580px;top:1022px;width:88px">Select a clinical need for referral</div>

  <div class="tray-steps">
    <span><b>1.</b> Right Click Icon</span><span><b>3.</b> Send to Pharmacist</span>
    <span><b>2.</b> Then press Refer this patient</span><span>Screen will Appear</span>
  </div>
  <div class="screen" style="left:686px;top:1136px;width:200px;height:50px" role="img" aria-label="Desktop taskbar with the bell icon in the system tray"></div>

  <div class="email"><span class="label">Email Us:</span><span class="addr">brightwellcarehmr@fernmail.example</span></div>

</main>
</body>
</html>
```